Minimalist, Flat(Matte) design for a Beef Jerky packaging company. No bullshit company looking for a

Need a packaging design for a new Beef Jerky product(in English). The name of the company is 'Vellorn' and thus the packaging should reflect the bullish, tough, and simple nature of the beef jerky product. The finished product should communicate simplicity, minimalism, yet toughness and strength.

The logo should be simple, with a minimal number of colors , and should be either all white/cream, or have some red as well. Main colors should be white, cream, tinted red, and matte black. I think 4 colors max would be best. The closest example to an existing package style would be Kessip Noir clove cigarettes( image attached).

It will be on a matte black standing pouch package. See image for package type. Package dimensions:

Dimension: Width x Gusset x Height
INCH : 5.125" (W) x 3.125" (G) x 8.125" (H)
MILLIMETER : 130mm (W) x 80mm (G) x 205mm (H)

I don't have anything totally specific so artistic liberty is encouraged, provided the colors are kept to a minimum and looks consistent with the simple nature of the brand and the matte black packaging.

Also attached an existing beef jerky package with a similar style to what we're looking for.

Industry/Entity Type

It Company

Colors
f59195
ffffff

Requirements
Must have
• Low contrast, flat and minimalist design.
Should not have
• A complicated design with many colors. Gawdy/flashy design. Bright colors. High contrast.

```html
<!DOCTYPE html>
<html lang="en">
<head>
<meta charset="utf-8">
<title>Vellorn Hand Crafted Beef Jerky – Peppered</title>
<link rel="stylesheet" href="https://fonts.googleapis.com/css2?family=Montserrat:wght@300;400;600&display=swap">
<style>
  :root {
    --backdrop: #746b62;
    --pouch-black: #141414;
    --pouch-shade: #1c1c1c;
    --brand-grey: #9a9a9a;
    --tagline-soft: #d9d9d9;
    --tagline-white: #f4f4f4;
    --flavour-red: #c8161d;
    --fine-print: #4a4a4a;
  }
  html, body {
    margin: 0;
    padding: 0;
    width: 1200px;
    height: 1108px;
    overflow: hidden;
    background: var(--backdrop);
    font-family: "Montserrat", sans-serif;
  }
  .canvas {
    position: relative;
    width: 1200px;
    height: 1108px;
  }
  .pouch-front {
    position: absolute;
    left: 342px;
    top: 195px;
    width: 540px;
    height: 805px;
    background: radial-gradient(ellipse at 55% 45%, var(--pouch-shade), var(--pouch-black) 70%);
    text-align: center;
    overflow: hidden;
  }
  .bull-artwork {
    position: absolute;
    left: 40px;
    top: 400px;
    width: 270px;
    height: 400px;
    border-radius: 45% 55% 0 0;
    background: radial-gradient(ellipse at 60% 35%, rgba(60,60,60,0.55), rgba(20,20,20,0) 70%);
  }
  .brand-name {
    position: absolute;
    left: 0;
    right: 0;
    top: 158px;
    margin: 0;
    font-weight: 600;
    font-size: 64px;
    letter-spacing: 1px;
    color: var(--brand-grey);
  }
  .tagline {
    position: absolute;
    left: 0;
    right: 0;
    top: 290px;
    margin: 0;
    line-height: 1.1;
  }
  .tagline-craft {
    display: block;
    font-weight: 300;
    font-size: 36px;
    color: var(--tagline-soft);
  }
  .tagline-product {
    display: block;
    font-weight: 400;
    font-size: 46px;
    color: var(--tagline-white);
    margin-top: 2px;
  }
  .flavour {
    position: absolute;
    left: 0;
    right: 0;
    top: 610px;
    margin: 0;
    font-weight: 300;
    font-size: 54px;
    color: var(--flavour-red);
  }
  .net-weight {
    position: absolute;
    left: 0;
    right: 0;
    top: 735px;
    margin: 0;
    font-weight: 300;
    font-size: 16px;
    color: var(--fine-print);
  }
</style>
</head>
<body>
  <main class="canvas">
    <section class="pouch-front">
      <div class="bull-artwork" role="img" aria-label="Faint engraved-style bull head illustration"></div>
      <h1 class="brand-name">VELLORN</h1>
      <p class="tagline">
        <span class="tagline-craft">Hand crafted</span>
        <span class="tagline-product">beef jerky</span>
      </p>
      <p class="flavour">Peppered</p>
      <p class="net-weight">Net weight: 3 oz/100g</p>
    </section>
  </main>
</body>
</html>
```